Building showcase catalogue for a post frame construction company

We are looking for a brochure for our clients showcasing our buildings. We are a post frame building company that makes commercial, ag, homes, and other building types. We are looking for a brochure that we can use with all the types of buildings simply by changing out the pictures. We would like a more photo heavy brochure thats 1-5 pages. We want the design to feel high end luxury. Our colors are black, white, and chrome. I will upload our logo as well as some building photos in the suburban category of our buildings. We would like a page to showcase some building layouts as well.

We need the size to be us letter size.

Industry/Entity Type

Construction

Font styles to use
Serif

Colors

Designer to choose only greyscale colors for use in the design.

Requirements
Must have
• A space to showcase building photos, small text space for information. An area to showcase building layouts.
Nice to have
• I would like to have a very clean professional look thats looks high end.
Should not have
• Areas for detail pictures. We mostly have exterior building shots.

```html
<!DOCTYPE html>
<html lang="en">
<head>
<meta charset="utf-8">
<title>Norland Builders Portfolio</title>
<link href="https://fonts.googleapis.com/css2?family=Oswald:wght@400;500&family=Arimo:wght@400;700&display=swap" rel="stylesheet">
<style>
  :root {
    --backdrop: #dcdcdc;
    --ink: #231f20;
    --paper: #ffffff;
    --rule-light: #ffffff;
    --rule-dark: #231f20;
    --text-soft: #c8c8c8;
    --plan-fill: #f2f2f2;
  }
  * { box-sizing: border-box; margin: 0; padding: 0; }
  html, body { width: 1200px; height: 1200px; overflow: hidden; background: var(--backdrop); }
  body { position: relative; font-family: "Arimo", Arial, sans-serif; }

  .page { position: absolute; width: 385px; height: 497px; overflow: hidden; box-shadow: 2px 3px 6px rgba(0,0,0,0.18); }
  .page--cover { left: 181px; top: 70px; background: var(--ink); }
  .page--feature { left: 634px; top: 70px; background: var(--ink); }
  .page--plan { left: 181px; top: 601px; background: var(--paper); }
  .page--interior { left: 634px; top: 601px; background: var(--ink); }

  .abs { position: absolute; }
  .headline {
    position: absolute; font-family: "Oswald", "Arial Narrow", sans-serif;
    font-weight: 400; line-height: 1; letter-spacing: -0.2px; white-space: nowrap;
  }
  .photo { position: absolute; }

  /* cover */
  .cover-photo-top { left: 204px; top: 99px; width: 135px; height: 81px;
    background: linear-gradient(165deg, #b4c4d4 0%, #dfe2e5 50%, #9ea190 100%); }
  .cover-photo-bottom { left: 204px; top: 190px; width: 135px; height: 81px;
    background: linear-gradient(165deg, #b9c6d2 0%, #a13038 55%, #7c8862 100%); }
  .cover-rule { left: 0; top: 293px; width: 385px; height: 1px; background: var(--rule-light); }
  .cover-namebox { left: 0; top: 294px; width: 181px; height: 172px; background: var(--paper);
    display: flex; align-items: center; justify-content: center; flex-direction: column; }
  .brand-name { font-family: "Arimo", Arial, sans-serif; font-weight: 700; color: var(--ink);
    font-size: 13px; letter-spacing: 1.5px; text-align: center; line-height: 1.3; }
  .cover-title { left: 204px; top: 345px; font-size: 36px; color: var(--paper); }
  .contact { left: 204px; font-size: 9px; color: var(--paper); font-weight: 700; white-space: nowrap; }
  .contact span { font-weight: 400; color: var(--text-soft); margin-right: 4px; }

  /* feature */
  .feature-photo { left: 0; top: 50px; width: 385px; height: 271px;
    background: linear-gradient(172deg, #a9c0d9 0%, #c5d0d8 25%, #9c3238 58%, #7f9d55 100%); }
  .feature-textbox { left: 158px; top: 321px; width: 227px; height: 150px; background: var(--paper); }
  .feature-rule-light { left: 68px; top: 366px; width: 90px; height: 1px; background: var(--rule-light); }
  .feature-rule-dark { left: 158px; top: 366px; width: 196px; height: 1px; background: var(--rule-dark); }
  .client-name { left: 28px; top: 397px; font-size: 26px; color: var(--paper); }
  .body-copy { font-size: 6.2px; line-height: 8.8px; }
  .feature-copy { left: 192px; top: 380px; width: 160px; color: var(--ink); }

  /* plan */
  .page-rule { left: 29px; top: 27px; width: 313px; height: 1px; }
  .page-num { left: 351px; top: 24px; font-size: 6px; }
  .plan-rule { background: var(--rule-dark); }
  .plan-num { color: var(--ink); }
  .plan-drawing { left: 114px; top: 59px; width: 240px; height: 320px;
    background: var(--plan-fill); }
  .plan-title { left: 27px; top: 419px; font-size: 26px; line-height: 0.98; color: var(--ink); }
  .spec-box { left: 113px; top: 402px; width: 272px; height: 82px; background: var(--ink); }
  .spec { position: absolute; font-size: 6.2px; color: var(--text-soft); white-space: nowrap; }
  .spec b { color: var(--paper); }

  /* interior */
  .interior-rule { background: var(--rule-light); opacity: 0.85; }
  .interior-num { color: var(--paper); }
  .interior-textbox { left: 0; top: 212px; width: 226px; height: 90px; background: var(--paper); }
  .interior-copy { left: 29px; top: 230px; width: 122px; color: var(--ink); }
  .room-living { left: 29px; top: 55px; width: 181px; height: 113px;
    background: linear-gradient(175deg, #d6d2c9 0%, #c4beb2 50%, #786f63 100%); }
  .room-bath { left: 174px; top: 136px; width: 181px; height: 112px;
    background: linear-gradient(160deg, #e3e0da 0%, #bdb6aa 55%, #8d8576 100%); }
  .room-kitchen { left: 174px; top: 267px; width: 181px; height: 112px;
    background: linear-gradient(175deg, #d4cfc6 0%, #b3a794 55%, #71685c 100%); }
  .room-dining { left: 29px; top: 348px; width: 181px; height: 113px;
    background: linear-gradient(175deg, #d1cdc4 0%, #bdb7ab 50%, #645b50 100%); }
  .interior-title-rule { left: 210px; top: 460px; width: 145px; height: 1px; background: var(--rule-light); }
  .interior-title { right: 30px; top: 433px; font-size: 26px; color: var(--paper); }
</style>
</head>
<body>

<section class="page page--cover">
  <div class="photo cover-photo-top" role="img" aria-label="Photo of a white two-storey post frame home with stone base"></div>
  <div class="photo cover-photo-bottom" role="img" aria-label="Photo of a red post frame home with wraparound porch"></div>
  <div class="abs cover-rule"></div>
  <div class="abs cover-namebox">
    <div class="brand-name">NORLAND<br>BUILDERS, INC.</div>
  </div>
  <h1 class="headline cover-title">PORTFOLIO</h1>
  <p class="abs contact" style="top:424px"><span>P |</span>(555) 201-4800</p>
  <p class="abs contact" style="top:440px"><span>F |</span>(555) 201-4801</p>
  <p class="abs contact" style="top:457px"><span>E |</span>info@norlandbuilders.com</p>
</section>

<section class="page page--feature">
  <div class="photo feature-photo" role="img" aria-label="Photo of a red post frame home with grey metal roof and garage door on a green lawn"></div>
  <div class="abs feature-textbox"></div>
  <div class="abs feature-rule-light"></div>
  <div class="abs feature-rule-dark"></div>
  <h2 class="headline client-name">DANA R.</h2>
  <p class="abs body-copy feature-copy">Lorem Ipsum is simply dummy text of the printing and typesetting industry. Lorem Ipsum has been the industry's standard dummy text ever since the 1500s, when an unknown printer took a galley of type and scrambled it to make a type specimen book. It has survived not only five centuries, but also the leap into electronic typesetting, remaining essentially unchanged.</p>
</section>

<section class="page page--plan">
  <div class="abs page-rule plan-rule"></div>
  <span class="abs page-num plan-num">2</span>
  <div class="abs plan-drawing" role="img" aria-label="Floor plan drawing of a one-bedroom home with garage, great room, master suite and covered porch"></div>
  <h2 class="headline plan-title">FLOOR<br>PLAN</h2>
  <div class="abs spec-box">
    <span class="spec" style="left:14px;top:17px">Square Feet</span><span class="spec" style="left:58px;top:17px">: <b>1584</b></span>
    <span class="spec" style="left:14px;top:30px">Bedrooms</span><span class="spec" style="left:58px;top:30px">: <b>1</b></span>
    <span class="spec" style="left:14px;top:43px">Bathrooms</span><span class="spec" style="left:58px;top:43px">: <b>1</b></span>
    <span class="spec" style="left:119px;top:17px">Exterior</span><span class="spec" style="left:187px;top:17px">: Vinyl Siding</span>
    <span class="spec" style="left:119px;top:30px">Roof Color</span><span class="spec" style="left:187px;top:30px">: Terratone</span>
    <span class="spec" style="left:119px;top:43px">Siding Color</span><span class="spec" style="left:187px;top:43px">: Autumn Red</span>
    <span class="spec" style="left:119px;top:56px">Special Features</span><span class="spec" style="left:187px;top:56px">: Overhangs</span>
  </div>
</section>

<section class="page page--interior">
  <div class="abs page-rule interior-rule"></div>
  <span class="abs page-num interior-num">3</span>
  <div class="abs interior-textbox"></div>
  <p class="abs body-copy interior-copy">Lorem Ipsum is simply dummy text of the printing and typesetting industry. Lorem Ipsum has been the industry's standard dummy text ever since the 1500s, when an unknown printer took a galley of type and scrambled it to make a type specimen book.</p>
  <div class="photo room-living" role="img" aria-label="Photo of a living room with sofas and wood floor"></div>
  <div class="photo room-bath" role="img" aria-label="Photo of a bathroom with wood vanity"></div>
  <div class="photo room-kitchen" role="img" aria-label="Photo of a kitchen with stainless fridge and island"></div>
  <div class="photo room-dining" role="img" aria-label="Photo of an open dining and living area"></div>
  <div class="abs interior-title-rule"></div>
  <h2 class="headline interior-title">INTERIOR</h2>
</section>

</body>
</html>
```